Business Cards

Business card design for my company.
I would like the card's background colour to be black. You can also see our web site to get an idea of our brand. https://www.dlqmarrowfield.com.au/
- Name
- Email

```html
<!DOCTYPE html>
<html lang="en">
<head>
<meta charset="utf-8">
<title>DLQ Marrowfield — Business Card</title>
<link href="https://fonts.googleapis.com/css2?family=Poppins:wght@400;500;600;700&display=swap" rel="stylesheet">
<style>
  :root {
    --stage: #5e5e5e;
    --card: #000000;
    --green: #0c9447;
    --white: #ffffff;
  }
  * { margin: 0; padding: 0; box-sizing: border-box; }
  html, body { width: 1200px; height: 1200px; overflow: hidden; }
  body {
    background: var(--stage);
    font-family: "Poppins", sans-serif;
    position: relative;
  }
  .card {
    position: absolute;
    left: 225px;
    width: 750px;
    height: 449px;
    background: var(--card);
    overflow: hidden;
  }
  .card--front { top: 120px; }
  .card--back { top: 630px; }

  .holder { position: absolute; left: 70px; top: 50px; color: var(--white); }
  .holder__name { font-size: 30px; font-weight: 600; line-height: 38px; letter-spacing: 0.5px; }
  .holder__title { color: var(--green); font-size: 19px; letter-spacing: 3px; line-height: 22px; }
  .holder__line { font-size: 15px; font-weight: 500; line-height: 22px; }

  .brand {
    position: absolute;
    display: flex;
    align-items: center;
    gap: 10px;
    color: var(--white);
    font-weight: 700;
  }
  .brand__square { background: var(--green); }
  .card--front .brand { right: 60px; top: 60px; font-size: 44px; }
  .card--front .brand__square { width: 20px; height: 20px; }
  .card--back .brand { left: 0; right: 0; top: 140px; justify-content: center; font-size: 96px; gap: 18px; }
  .card--back .brand__square { width: 36px; height: 36px; }

  .headline {
    position: absolute;
    left: 0; right: 0;
    text-align: center;
    color: var(--green);
    font-size: 44px;
    font-weight: 700;
    letter-spacing: 0.3px;
  }
  .card--front .headline { top: 170px; }
  .card--back .headline { top: 316px; }

  .contacts { position: absolute; left: 70px; top: 250px; list-style: none; color: var(--white); }
  .contacts li { display: flex; align-items: center; gap: 10px; font-size: 23px; height: 33px; }
  .contacts svg { width: 24px; height: 24px; flex: none; }

  .address-band {
    position: absolute;
    left: 0; right: 0; bottom: 0;
    height: 83px;
    background: var(--green);
    color: var(--white);
    font-size: 25px;
    display: flex;
    align-items: center;
    padding-left: 25px;
  }
</style>
</head>
<body>
  <section class="card card--front">
    <div class="holder">
      <p class="holder__name">Xxxx Xxxx</p>
      <p class="holder__title">XXXXXXX</p>
      <p class="holder__line">X xxx - 010101-0101</p>
    </div>
    <div class="brand"><span class="brand__square"></span>DLQ</div>
    <h1 class="headline">DLQ MARROWFIELD</h1>
    <ul class="contacts">
      <li>
        <svg viewBox="0 0 24 24"><circle cx="12" cy="12" r="11" fill="var(--green)"/><path d="M8.5 6.5l2 2.5-1.2 1.4c.8 1.6 2 2.8 3.6 3.6l1.4-1.2 2.5 2-1.3 1.8c-4 0-8.8-4.8-8.8-8.8z" fill="#000"/></svg>
        <span>phone : (0101) 010-0101</span>
      </li>
      <li>
        <svg viewBox="0 0 24 24"><rect x="1" y="5" width="22" height="15" fill="var(--green)"/><path d="M1 5l11 9 11-9M1 20l8-7M23 20l-8-7" stroke="#000" stroke-width="1.5" fill="none"/></svg>
        <span>email : xxx@dlqmarrowfield.com</span>
      </li>
      <li>
        <svg viewBox="0 0 24 24" fill="none" stroke="var(--green)" stroke-width="1.8"><circle cx="12" cy="12" r="10"/><ellipse cx="12" cy="12" rx="4.5" ry="10"/><path d="M2 12h20M4 7h16M4 17h16"/></svg>
        <span>website : www.dlqmarrowfield.com</span>
      </li>
    </ul>
    <div class="address-band">4820 Harbor Lane Suite 310, Fairmont Bay, CA 90417</div>
  </section>

  <section class="card card--back">
    <div class="brand"><span class="brand__square"></span>DLQ</div>
    <h2 class="headline">DLQ MARROWFIELD</h2>
  </section>
</body>
</html>
```